Brennock transport business cards

Front of card, Looking for my logo on one side of the card

Back of card,
Brennock Transport Maintenance
Onsite Cars, Trucks & trailer maintenance and repairs
Gary Brennock
0452918406
Brennocktm@vexmail.test

```html
<!DOCTYPE html>
<html lang="en">
<head>
<meta charset="utf-8">
<title>Brennock Transport Maintenance – Business Cards</title>
<link href="https://fonts.googleapis.com/css2?family=Montserrat:wght@500;600;700;800&display=swap" rel="stylesheet">
<style>
  :root {
    --stage: #2b2b2c;
    --card-dark: #1b1b1c;
    --card-light: #ffffff;
    --brand-blue: #1f6bbf;
    --ink: #141414;
    --ink-soft: #3a3a3a;
    --white: #ffffff;
  }
  * { box-sizing: border-box; margin: 0; padding: 0; }
  html, body {
    width: 1200px; height: 875px; overflow: hidden;
    background: var(--stage);
    font-family: "Montserrat", sans-serif;
  }
  .stage {
    position: relative; width: 1200px; height: 875px;
  }
  .card {
    position: absolute;
    width: 600px; height: 343px;
    border-radius: 22px;
    overflow: hidden;
    box-shadow: 0 18px 40px rgba(0,0,0,.45);
  }
  .card--front { left: 110px; top: 70px; background: var(--card-dark); }
  .card--back  { left: 490px; top: 462px; background: var(--card-light); }

  .card__band {
    position: absolute; left: 0; bottom: 0; width: 100%; height: 44px;
  }
  .card__band path { fill: var(--brand-blue); }

  /* front */
  .front-lockup {
    position: absolute; left: 70px; top: 78px; right: 40px;
    color: var(--white);
  }
  .brand-name {
    display: flex; align-items: center; gap: 12px;
    font-weight: 700; font-size: 30px; letter-spacing: .5px;
    text-transform: uppercase; line-height: 1.1;
  }
  .brand-name__mark {
    width: 18px; height: 18px; background: var(--brand-blue); flex: none;
  }
  .brand-sub {
    margin-top: 6px; padding-left: 30px;
    font-weight: 700; font-size: 18px; letter-spacing: 2px; text-transform: uppercase;
  }
  .brand-rule {
    margin: 12px 0 14px 30px; height: 3px; width: 420px; background: var(--brand-blue);
  }
  .front-phone {
    font-weight: 800; font-size: 64px; letter-spacing: 4px; line-height: 1;
  }

  /* back */
  .back-layout {
    position: absolute; left: 44px; top: 92px; right: 30px;
    display: flex; align-items: stretch; gap: 22px;
  }
  .back-brand { color: var(--ink); padding-top: 14px; }
  .back-brand .brand-name { font-size: 19px; gap: 8px; }
  .back-brand .brand-name__mark { width: 12px; height: 12px; }
  .back-brand .brand-sub { font-size: 11px; letter-spacing: 1px; padding-left: 20px; margin-top: 4px; }
  .back-brand .brand-rule { width: 220px; height: 2px; margin: 7px 0 8px 20px; }
  .back-phone { font-weight: 800; font-size: 34px; letter-spacing: 2px; line-height: 1; }

  .back-divider { width: 1.5px; background: var(--brand-blue); }

  .contact { color: var(--ink-soft); padding-top: 6px; }
  .contact__name {
    color: var(--brand-blue); font-weight: 700; font-size: 24px; margin-bottom: 12px;
  }
  .contact__line {
    display: flex; align-items: center; gap: 8px;
    font-weight: 500; font-size: 13.5px; margin-bottom: 8px;
  }
  .contact__icon { width: 12px; height: 10px; flex: none; }
  .contact__icon path, .contact__icon rect { fill: var(--brand-blue); }
  .contact__tagline { font-weight: 500; font-size: 13.5px; line-height: 1.35; max-width: 200px; }
</style>
</head>
<body>
<main class="stage">

  <section class="card card--front" aria-label="Card front">
    <div class="front-lockup">
      <div class="brand-name"><span class="brand-name__mark"></span>Brennock</div>
      <div class="brand-sub">Transport Maintenance</div>
      <div class="brand-rule"></div>
      <div class="front-phone">0452918406</div>
    </div>
    <svg class="card__band" viewBox="0 0 600 44" preserveAspectRatio="none" aria-hidden="true">
      <path d="M0 28 H560 Q590 28 600 4 V44 H0 Z"/>
    </svg>
  </section>

  <section class="card card--back" aria-label="Card back">
    <div class="back-layout">
      <div class="back-brand">
        <div class="brand-name"><span class="brand-name__mark"></span>Brennock</div>
        <div class="brand-sub">Transport Maintenance</div>
        <div class="brand-rule"></div>
        <div class="back-phone">0452918406</div>
      </div>
      <div class="back-divider"></div>
      <div class="contact">
        <div class="contact__name">Gary Brennock</div>
        <div class="contact__line">
          <svg class="contact__icon" viewBox="0 0 12 10" aria-hidden="true">
            <rect x="0" y="1" width="12" height="8" rx="1"/>
            <path d="M0 1.5 L6 6 L12 1.5" fill="none" stroke="#fff" stroke-width="1.2"/>
          </svg>
          Brennocktm@vexmail.test
        </div>
        <p class="contact__tagline">Onsite Cars, Trucks &amp; trailer maintenance and repairs</p>
      </div>
    </div>
    <svg class="card__band" viewBox="0 0 600 44" preserveAspectRatio="none" aria-hidden="true">
      <path d="M0 28 H560 Q590 28 600 4 V44 H0 Z"/>
    </svg>
  </section>

</main>
</body>
</html>
```